Need a website for our company

We need a website for our company to showcase all our work for customers to see.
We do all phases of home improvement:
Dormers/Extensions
Basement Remodel
Masonry/Concrete/Pavers/Asphalt
Cultured Stone Veneer
Kitchens
Bathrooms
Pool designs
Outdoor Bathroom
Outdoor Kitchens
Tile work
For reference, something similar to this website: https://brightoakrenovations.example/
Target Market(s)
We are trying to target homeowners.
Coding
Number of Pages Required
Look and feel

```html
<!DOCTYPE html>
<html lang="en">
<head>
<meta charset="utf-8">
<title>Bright Oak Renovations</title>
<link rel="stylesheet" href="https://fonts.googleapis.com/css2?family=Montserrat:wght@400;500;600;700;800&family=Oswald:wght@500;600&family=Kaushan+Script&display=swap">
<style>
:root{
  --black:#000;
  --ink:#111;
  --dark:#2a2a2a;
  --footer:#1d1d1d;
  --white:#fff;
  --gold:#c89d2c;
  --gold-text:#f0c419;
  --tag:#e6e6e6;
  --tag-active:#6f6f6f;
  --muted:#555;
}
*{box-sizing:border-box;margin:0;padding:0}
html,body{width:1200px;height:3732px;overflow:hidden}
body{position:relative;font-family:'Montserrat',sans-serif;color:var(--ink);background:var(--white)}
.abs{position:absolute}
.center{left:0;width:1200px;text-align:center}

/* header */
.site-header{top:0;left:0;width:1200px;height:83px;background:var(--black);color:var(--white)}
.brand{left:26px;top:22px;font-weight:700;font-size:17px;display:flex;align-items:center;gap:8px;color:var(--white)}
.brand .dot{width:14px;height:14px;border:2px solid var(--white)}
.call{right:26px;top:4px;display:flex;align-items:center;gap:8px}
.call small{display:block;font-size:11px;font-weight:500}
.call strong{font-size:20px;font-weight:600;letter-spacing:.5px}
.main-nav{right:26px;top:62px;display:flex;gap:42px;font-size:12px;font-weight:500}

/* hero */
.hero{top:83px;left:0;width:1200px;height:542px;background:linear-gradient(180deg,#5b4b3c 0%,#6b6a55 45%,#5b7a34 75%,#4a6a22 100%)}
.hero h1{top:102px;color:var(--white);font-weight:800;font-size:58px;line-height:65px;letter-spacing:1px;text-shadow:0 2px 6px rgba(0,0,0,.5)}
.btn{display:flex;align-items:center;justify-content:center;gap:10px;background:var(--black);color:var(--white);border-radius:24px;font-weight:500;font-size:18px;letter-spacing:.5px}
.hero .btn{left:438px;top:343px;width:326px;height:46px}

/* section titles */
.script{font-family:'Kaushan Script',cursive;font-size:28px;color:#333}
.title{font-size:32px;font-weight:500;letter-spacing:1px}

/* services */
.card{width:217px;height:124px;border-radius:4px;overflow:hidden;color:var(--white);display:flex;align-items:center;justify-content:center;text-align:center;font-family:'Oswald',sans-serif;font-weight:600;font-size:16px;letter-spacing:.5px;text-shadow:0 1px 3px rgba(0,0,0,.8);line-height:20px}
.card.featured{background:#1a1a1a;flex-direction:column;text-shadow:none}
.card.featured h3{font-family:'Oswald',sans-serif;color:var(--gold-text);font-size:16px;font-weight:600}
.card.featured p{font-family:'Montserrat',sans-serif;font-weight:400;font-size:11px;line-height:14px;margin:6px 20px}
.card.featured a{font-family:'Montserrat',sans-serif;font-weight:500;color:var(--gold-text);font-size:11px;text-decoration:none}

/* about */
.about-photo{left:41px;top:1285px;width:534px;height:357px;background:linear-gradient(160deg,#bcd3ea 0%,#8c7060 40%,#6f8f45 80%,#4f7a2a 100%);border-radius:4px;box-shadow:-6px -6px 0 #000}
.about-text{left:626px;top:1328px;width:550px;font-size:13px;line-height:21px;color:#333}
.stat{width:160px;height:75px;border:1px solid #ccc;box-shadow:0 2px 6px rgba(0,0,0,.25);text-align:center;padding-top:10px}
.stat b{display:block;font-size:25px;font-weight:400}
.stat span{font-size:12px;color:#333}

/* before/after */
.compare{top:1710px;left:0;width:1200px;height:490px;background:linear-gradient(90deg,#1f1f1f,#3a3a3a 50%,#1f1f1f)}
.panel{top:1763px;width:312px;height:383px;display:flex;align-items:flex-end;justify-content:center;padding-bottom:28px;font-size:30px;color:#111}
.panel.before{left:287px;background:linear-gradient(180deg,#a08a6c 0%,#8b7a62 60%,#6e6a66 100%)}
.panel.after{left:600px;background:linear-gradient(180deg,#efefec 0%,#e3e2dc 60%,#c7813a 100%)}
.arrow-btn{width:72px;height:72px;border-radius:50%;background:#000;display:flex;align-items:center;justify-content:center}

/* projects */
.tag{height:30px;background:var(--tag);font-size:17px;padding:0 11px;display:flex;align-items:center;color:#222}
.tag.active{background:var(--tag-active);color:var(--white)}
.tag-row{display:flex;justify-content:center;gap:20px}
.project{top:2488px;width:275px;height:274px;border-radius:3px;overflow:hidden}
.project .label{position:absolute;left:0;bottom:0;width:100%;height:38px;background:rgba(0,0,0,.75);color:var(--white);font-size:17px;display:flex;align-items:center;justify-content:center}

/* why choose */
.why{top:2910px;left:0;width:1200px;height:427px;background:linear-gradient(180deg,#2c2a27,#1e1d1b)}
.why .script{color:#ddd}
.why .title{color:var(--white)}
.why-lead{top:3069px;color:var(--white);font-size:15px;line-height:21px}
.feature{top:3170px;display:flex;gap:10px;width:290px}
.feature h4{color:var(--gold-text);font-weight:500;font-size:17px;line-height:18px}
.feature p{color:var(--white);font-size:12px;line-height:15px;margin-top:3px}
.divider{top:3150px;width:1px;height:125px;background:#666}

/* call band */
.call-band{top:3337px;left:0;width:1200px;height:99px;background:var(--gold);color:var(--white);display:flex;align-items:center;justify-content:center;gap:40px}
.call-band span{font-size:25px}
.call-band strong{font-size:52px;font-weight:500;letter-spacing:1px;display:flex;align-items:center;gap:14px}

/* footer */
.site-footer{top:3436px;left:0;width:1200px;height:296px;background:var(--footer);color:var(--white)}
.footer-brand{left:45px;top:40px;font-size:22px;font-weight:700;display:flex;align-items:center;gap:10px}
.footer-brand .dot{width:18px;height:18px;border:2px solid var(--white)}
.social{top:150px;display:flex;gap:12px;left:45px}
.social span{width:48px;height:48px;background:#3b3b3b;border:1px solid #777;display:block}
.foot-h{font-size:17px;font-weight:500}
.foot-links{list-style:none;font-size:12px;font-weight:500;line-height:31px}
.addr{font-size:13px;line-height:20px;display:flex;gap:12px;align-items:flex-start}
.copyright{top:258px;color:#777;font-size:15px}
</style>
</head>
<body>

<header class="site-header abs">
  <div class="brand abs"><span class="dot"></span>Bright Oak Renovations</div>
  <div class="call abs">
    <svg width="36" height="36" viewBox="0 0 24 24" fill="none" stroke="#fff" stroke-width="1.8"><path d="M6.6 10.8a15 15 0 0 0 6.6 6.6l2.2-2.2a1 1 0 0 1 1-.25 11.4 11.4 0 0 0 3.6.6 1 1 0 0 1 1 1V20a1 1 0 0 1-1 1A17 17 0 0 1 3 4a1 1 0 0 1 1-1h3.5a1 1 0 0 1 1 1c0 1.25.2 2.45.57 3.57a1 1 0 0 1-.25 1z"/><path d="M15 3a6 6 0 0 1 6 6M15 6.5A2.5 2.5 0 0 1 17.5 9"/></svg>
    <div><small>Call Us</small><strong>(516) XXX-XXXX</strong></div>
  </div>
  <nav class="main-nav abs"><span>HOME</span><span>ABOUT US</span><span>SERVICES</span><span>OUR WORK</span><span>CONTACT US</span></nav>
</header>

<section class="hero abs" role="img" aria-label="Family sitting on the lawn in front of a brick home">
  <h1 class="abs center">EXPERIENCED AND TRUSTED<br>HOME EXTENSION AND<br>RENOVATION BUILDERS</h1>
  <div class="btn abs">GET YOUR FREE&nbsp; ESTIMATE</div>
</section>

<div class="script abs center" style="top:688px">Our Service</div>
<h2 class="title abs center" style="top:720px">What We Do</h2>

<div class="card featured abs" style="left:25px;top:785px">
  <h3>DORMERS/EXTENSIONS</h3>
  <p>Lorem ipsum dolor sit amet, consectetur ...</p>
  <a>Learn More ⟶</a>
</div>
<div class="card abs" style="left:258px;top:785px;background:linear-gradient(135deg,#d9d4cc,#6f5a48)" role="img" aria-label="Finished basement remodel">BASEMENT REMODEL</div>
<div class="card abs" style="left:491px;top:785px;background:linear-gradient(135deg,#8d8a85,#5b5048)" role="img" aria-label="Workers laying pavers">MASONRY/CONCRETE/<br>PAVERS/ASPHALT</div>
<div class="card abs" style="left:725px;top:785px;background:linear-gradient(135deg,#a59a86,#6c6458)" role="img" aria-label="Cultured stone veneer wall">CULTURED STONE VENEER</div>
<div class="card abs" style="left:958px;top:785px;background:linear-gradient(135deg,#c9c5bf,#8a7a6c)" role="img" aria-label="Modern kitchen">KITCHENS</div>
<div class="card abs" style="left:25px;top:927px;background:linear-gradient(135deg,#4a3d30,#b09a7c)" role="img" aria-label="Bathroom interior">BATHROOMS</div>
<div class="card abs" style="left:258px;top:927px;background:linear-gradient(135deg,#2d8fc4,#6fcbe8)" role="img" aria-label="Swimming pool">POOL DESIGNS</div>
<div class="card abs" style="left:491px;top:927px;background:linear-gradient(135deg,#2f5b2c,#c9cbc2)" role="img" aria-label="Outdoor bathroom with plants">OUTDOOR BATHROOM</div>
<div class="card abs" style="left:725px;top:927px;background:linear-gradient(135deg,#5d84b8,#4d4a45)" role="img" aria-label="Outdoor kitchen">OUTDOOR KITCHENS</div>
<div class="card abs" style="left:958px;top:927px;background:linear-gradient(135deg,#e0ddd8,#9a6a40)" role="img" aria-label="Tile installation">TILE WORK</div>

<div class="btn abs" style="left:438px;top:1077px;width:326px;height:46px">VIEW ALL SERVICES</div>

<div class="script abs center" style="top:1186px">About Us</div>
<h2 class="title abs center" style="top:1219px">Who We Are</h2>
<div class="about-photo abs" role="img" aria-label="Family walking outside their renovated home"></div>
<p class="about-text abs">Lorem ipsum dolor sit amet, consectetur adipiscing elit, sed do eiusmod tempor incididunt ut labore et dolore magna aliqua. Quis ipsum suspendisse ultrices gravida. Risus commodo viverra maecenas accumsan lacus vel facilisis.</p>
<div class="btn abs" style="left:662px;top:1446px;width:242px;height:45px">MORE ABOUT US ⟶</div>
<div class="stat abs" style="left:627px;top:1568px"><b>30</b><span>Years of Experience</span></div>
<div class="stat abs" style="left:820px;top:1568px"><b>12k+</b><span>Projects Completed</span></div>
<div class="stat abs" style="left:1013px;top:1568px"><b>10k+</b><span>Happy Clients</span></div>

<section class="compare abs" role="img" aria-label="Dark room interior backdrop"></section>
<div class="panel before abs" role="img" aria-label="Room before renovation">Before</div>
<div class="panel after abs" role="img" aria-label="Room after renovation">After</div>
<div class="arrow-btn abs" style="left:119px;top:1920px"><svg width="26" height="32" viewBox="0 0 26 32"><path d="M19 3L7 16l12 13" fill="none" stroke="#fff" stroke-width="5"/></svg></div>
<div class="arrow-btn abs" style="left:1007px;top:1920px"><svg width="26" height="32" viewBox="0 0 26 32"><path d="M7 3l12 13L7 29" fill="none" stroke="#fff" stroke-width="5"/></svg></div>

<div class="script abs center" style="top:2262px">Feauture Projects</div>
<h2 class="title abs center" style="top:2295px">Our Projects</h2>
<div class="tag-row abs center" style="top:2370px">
  <span class="tag active">Dormers/Extensions</span><span class="tag">Basement Remodel</span><span class="tag">Masonry/Concrete/Pavers/Asphalt</span><span class="tag">Cultured Stone Veneer</span>
</div>
<div class="tag-row abs center" style="top:2416px">
  <span class="tag">Kitchens</span><span class="tag">Bathrooms</span><span class="tag">Pool designs</span><span class="tag">Outdoor Bathroom</span><span class="tag">Outdoor Kitchens</span><span class="tag">Tile work</span>
</div>
<div class="project abs" style="left:25px;background:linear-gradient(160deg,#2f6fc4,#e9e4da 50%,#c2522c)" role="img" aria-label="Dormer with tiled roof"><div class="label">Project Name</div></div>
<div class="project abs" style="left:316px;background:linear-gradient(180deg,#8db4e0,#8a3c2e 55%,#5d7a3a)" role="img" aria-label="Brick house extension"><div class="label">Project Name</div></div>
<div class="project abs" style="left:608px;background:linear-gradient(135deg,#5a5a5a,#d17a55 50%,#6a5a50)" role="img" aria-label="Copper clad dormer"><div class="label">Project Name</div></div>
<div class="project abs" style="left:900px;background:linear-gradient(180deg,#3f7fcf,#eae7e1 50%,#c2532c)" role="img" aria-label="Roof dormer window"><div class="label">Project Name</div></div>
<div class="btn abs" style="left:458px;top:2798px;width:282px;height:45px">VIEW ALL PROJECTS ⟶</div>

<section class="why abs" role="img" aria-label="Dim renovation workspace backdrop"></section>
<div class="script abs center" style="top:2972px;color:#ddd">Why Like Us</div>
<h2 class="title abs center" style="top:3012px;color:#fff">Why Choose Us</h2>
<p class="why-lead abs center">There are many Variations of passages of Lorem Ipsum abailable, But the<br>Majority have suffered alteration.</p>

<div class="feature abs" style="left:113px">
  <svg width="50" height="50" viewBox="0 0 50 50" fill="none" stroke="#f0c419" stroke-width="2.5"><path d="M25 44S5 30 5 17a10 10 0 0 1 20-3 10 10 0 0 1 20 3c0 13-20 27-20 27z"/><path d="M14 26l8 6 12-10"/></svg>
  <div><h4>We Care</h4><p>Lorem ipsum dolor sit amet, consectetur adipiscing elit, sed do eiusmod tempor incididunt ut labore et dolore magna</p></div>
</div>
<div class="divider abs" style="left:419px"></div>
<div class="feature abs" style="left:468px">
  <svg width="50" height="50" viewBox="0 0 50 50" fill="none" stroke="#f0c419" stroke-width="2.5"><rect x="5" y="9" width="36" height="34" rx="3"/><path d="M5 18h36M14 4v9M32 4v9"/><circle cx="38" cy="38" r="9" fill="#222"/><path d="M38 33v5l3 2"/></svg>
  <div><h4>Customer Service with Extened Hour</h4><p>Lorem ipsum dolor sit amet, consectetur adipiscing elit, sed do eiusmod tempor incididunt</p></div>
</div>
<div class="divider abs" style="left:777px"></div>
<div class="feature abs" style="left:830px">
  <svg width="50" height="50" viewBox="0 0 50 50" fill="none" stroke="#f0c419" stroke-width="2.5"><path d="M12 8l8-3h10l8 3 4 10v25H8V18z"/><path d="M20 5v38M30 5v38M8 28h34"/></svg>
  <div><h4>Safety Matters</h4><p>Lorem ipsum dolor sit amet, consectetur adipiscing elit, sed do eiusmod tempor incididunt</p></div>
</div>

<div class="call-band abs">
  <span>For Project Queries Call to Us at</span>
  <strong><svg width="54" height="54" viewBox="0 0 24 24" fill="none" stroke="#fff" stroke-width="1.8"><path d="M6.6 10.8a15 15 0 0 0 6.6 6.6l2.2-2.2a1 1 0 0 1 1-.25 11.4 11.4 0 0 0 3.6.6 1 1 0 0 1 1 1V20a1 1 0 0 1-1 1A17 17 0 0 1 3 4a1 1 0 0 1 1-1h3.5a1 1 0 0 1 1 1c0 1.25.2 2.45.57 3.57a1 1 0 0 1-.25 1z"/><path d="M15 3a6 6 0 0 1 6 6M15 6.5A2.5 2.5 0 0 1 17.5 9"/></svg>(516) XXX-XXXX</strong>
</div>

<footer class="site-footer abs">
  <div class="footer-brand abs"><span class="dot"></span>Bright Oak Renovations</div>
  <div class="social abs" aria-label="Social media links"><span></span><span></span><span></span></div>
  <div class="abs" style="left:526px;top:33px">
    <div class="foot-h">MENU</div>
    <ul class="foot-links" style="margin-left:4px;margin-top:6px"><li>HOME</li><li>ABOUT US</li><li>SERVICES</li><li>OUR WORK</li><li>CONTACT US</li></ul>
  </div>
  <div class="abs" style="left:917px;top:33px">
    <div class="foot-h">PHYSICAL ADDRESS:</div>
    <div class="addr" style="margin-top:14px"><svg width="18" height="26" viewBox="0 0 18 26"><path d="M9 1a8 8 0 0 0-8 8c0 6 8 16 8 16s8-10 8-16a8 8 0 0 0-8-8z" fill="#999"/><circle cx="9" cy="9" r="3" fill="#1d1d1d"/></svg><span>Lorem ipsum dolor sit amet,<br>consectetur adipiscing</span></div>
    <div class="addr" style="margin-top:14px"><svg width="18" height="20" viewBox="0 0 24 24" fill="#999"><path d="M6.6 10.8a15 15 0 0 0 6.6 6.6l2.2-2.2a1 1 0 0 1 1-.25 11.4 11.4 0 0 0 3.6.6 1 1 0 0 1 1 1V20a1 1 0 0 1-1 1A17 17 0 0 1 3 4a1 1 0 0 1 1-1h3.5a1 1 0 0 1 1 1c0 1.25.2 2.45.57 3.57a1 1 0 0 1-.25 1z"/></svg><span>(657) XXX XXXX</span></div>
    <div class="addr" style="margin-top:18px"><svg width="22" height="16" viewBox="0 0 22 16" fill="none" stroke="#999" stroke-width="1.5"><rect x="1" y="1" width="20" height="14"/><path d="M1 1l10 8 10-8"/></svg><span>info@brightoakrenovations.example</span></div>
  </div>
  <div class="copyright abs center">© 2023 Bright Oak Renovations Inc.</div>
</footer>

</body>
</html>
```